Brazilian wine business need a label for a sparkling wine

We are importing a new italian sparkling wine, but we need to build our own brand. Our main focus is to sell sparkling wine for events, specially for weddings. So, specially for this audience, presentation is key.
We like to see wine in a "uncomplicated" way.
It is a mid price product.
The foil capsule color must be black, white or silver, due to production restrictions. We cannot have any graphic interference in this part, also.

We need to develop a label for it. The name will be "Lumera Brut" (means "hug" in italian).

Our main public is people around the early 30s, so it should look modern and clean.
It is good, but not mandatory, to have a few information at the front label:
- Alcohol % (12%)
- Origin (Italy)

We need to avoid a few colours, for different reasons:
- Don´t use yellow/orange: too linked to Maison Dravelle;
- Don´t use red or pink: people think it is a rosé, but it is a white.
Our idea is to work with white and blue or turquoise, maybe a green, something like that. Can have a touch of gold, also. (more references in the color tab below)
- The bottle is black.

Industry/Entity Type

Business

Font styles to use
Other font styles liked:
• Berlin Sans FB Regular or something less "round" but similar to Cooper Black Regular

Colors
00a990
33b8a4

Requirements
Must have
• As the name means "hug", we want to have a graphic symbol that represents connections, alliances, symbiosis or infinite. I attached a few symbols that could be explore, but of course you can bring differente suggestions.
• We need a clean design, nothing with too many information.

```html
<!DOCTYPE html>
<html lang="en">
<head>
<meta charset="UTF-8">
<title>Lumera Brut — Front Label</title>
<link href="https://fonts.googleapis.com/css2?family=Fredoka:wght@500;600&family=Poppins:wght@400;500&display=swap" rel="stylesheet">
<style>
  :root {
    --aqua-band: #bfeee7;
    --aqua-line: #33b8a4;
    --teal-deep: #00a990;
    --paper: #f5f5f2;
    --ink: #1f2a2a;
    --ink-soft: #3c4646;
  }
  html, body {
    margin: 0;
    padding: 0;
    overflow: hidden;
  }
  body {
    width: 841px;
    height: 1200px;
    background: var(--paper);
  }
  .label {
    position: relative;
    width: 841px;
    height: 1200px;
    background: var(--paper);
    overflow: hidden;
  }
  .label__band {
    position: absolute;
    inset: 0 0 auto 0;
    width: 841px;
    height: 560px;
  }
  .brand-mark {
    position: absolute;
    top: 150px;
    left: 0;
    width: 841px;
    display: flex;
    justify-content: center;
    align-items: center;
    gap: 22px;
    font-family: "Fredoka", sans-serif;
    font-weight: 500;
    font-size: 58px;
    color: var(--teal-deep);
  }
  .brand-mark__dot {
    width: 40px;
    height: 40px;
    border-radius: 50%;
    border: 5px solid var(--teal-deep);
    box-sizing: border-box;
  }
  .product-name {
    position: absolute;
    top: 700px;
    left: 0;
    width: 841px;
    margin: 0;
    text-align: center;
    font-family: "Fredoka", sans-serif;
    font-weight: 600;
    font-size: 128px;
    letter-spacing: -1px;
    color: var(--ink);
  }
  .product-facts {
    position: absolute;
    top: 900px;
    left: 140px;
    margin: 0;
    padding: 0;
    list-style: none;
    font-family: "Poppins", sans-serif;
    font-weight: 500;
    font-size: 36px;
    line-height: 1.45;
    color: var(--ink-soft);
  }
</style>
</head>
<body>
  <main class="label">
    <svg class="label__band" viewBox="0 0 841 560" aria-hidden="true">
      <path d="M0 0 H841 V470 C760 440 700 520 610 500 C520 480 470 420 380 450 C290 480 220 540 130 520 C70 506 30 470 0 480 Z" fill="var(--aqua-band)"/>
      <path d="M0 480 C30 470 70 506 130 520 C220 540 290 480 380 450 C470 420 520 480 610 500 C700 520 760 440 841 470" fill="none" stroke="var(--aqua-line)" stroke-width="3"/>
    </svg>

    <div class="brand-mark">
      <span class="brand-mark__dot"></span>
      <span class="brand-mark__name">Lumera</span>
    </div>

    <h1 class="product-name">Lumera Brut</h1>

    <ul class="product-facts">
      <li>Alcohol: 12%</li>
      <li>Origin: Italy</li>
    </ul>
  </main>
</body>
</html>
```